Pennick - Eggs For Sale Sign

Would like a graphic quality image of a EGGS FOR SALE SIGN ... am getting a local outdoor sign company to print the sign and attach it to a frame.

this is going to be outside by the gate to our farm ... would like the sign to "POP" ... DRAW ATTENTION ... as it were ... please.

I think we need it about 36”(w) x 30”(h) ... maybe 48”x36” ... not sure ... need about an extra 1 1/2” border around also so that we can frame this into a wooden frame ...

The color picture is similar to the pattern we like ... the fonts you are welcome to just blow us out of the water with ... we are not tied down to any particular font ... like the “WANTED” posters of old ... sorta.

Logo Text

Quill Bend Acres

Colors

Designer to choose colors to be used in the design.

Requirements
Must have
• Some type of Fire Fly art ... not to modern ... not too comic book ...
Nice to have
• phone number
• call or text

```html
<!DOCTYPE html>
<html lang="en">
<head>
<meta charset="utf-8">
<title>Quill Bend Acres – Eggs For Sale Sign</title>
<link href="https://fonts.googleapis.com/css2?family=Alfa+Slab+One&family=Oswald:wght@600&family=Archivo+Black&family=Arimo:wght@700&display=swap" rel="stylesheet">
<style>
  :root {
    --page: #ffffff;
    --frame-dark: #3a1e0c;
    --frame-mid: #7a3f17;
    --frame-light: #a45a22;
    --plank-light: #a58b6e;
    --plank-mid: #8c7358;
    --plank-dark: #6e5a45;
    --seam: #231a12;
    --ink-white: #ffffff;
    --ink-black: #111111;
    --teal: #7fbcb6;
    --teal-deep: #3d8c88;
    --shadow: rgba(0,0,0,0.55);
  }
  * { margin: 0; padding: 0; box-sizing: border-box; }
  html, body { width: 1200px; height: 923px; overflow: hidden; background: var(--page); }
  .canvas { position: relative; width: 1200px; height: 923px; }
  .sign-frame {
    position: absolute; left: 78px; top: 110px; width: 1050px; height: 700px;
    background: linear-gradient(90deg, var(--frame-dark), var(--frame-mid) 8%, var(--frame-light) 50%, var(--frame-mid) 92%, var(--frame-dark));
  }
  .sign-panel {
    position: absolute; left: 40px; top: 52px; width: 966px; height: 596px;
    background: linear-gradient(180deg, var(--plank-mid), var(--plank-light) 30%, var(--plank-mid) 60%, var(--plank-light) 85%, var(--plank-dark));
    box-shadow: inset 0 0 40px rgba(0,0,0,0.45);
  }
  .wood-grain { position: absolute; inset: 0; }
  .layer { position: absolute; left: 0; top: 0; width: 1200px; height: 923px; }
  .brand {
    position: absolute; left: 0; top: 170px; width: 1200px; text-align: center;
    font-family: "Alfa Slab One", serif; font-size: 60px; color: var(--ink-white);
    letter-spacing: 2px; text-shadow: 3px 4px 4px var(--shadow); white-space: nowrap;
  }
  .brand-dot {
    display: inline-block; width: 26px; height: 26px; border-radius: 50%;
    background: var(--ink-white); margin: 0 18px; vertical-align: 8px;
  }
  .tagline {
    position: absolute; left: 0; top: 380px; width: 1206px; text-align: center;
    font-family: "Oswald", sans-serif; font-weight: 600; font-size: 40px;
    color: var(--ink-white); letter-spacing: 2px; transform: scaleY(1.15);
    text-shadow: 2px 3px 3px var(--shadow);
  }
  .product {
    position: absolute; left: 0; top: 452px; width: 1206px; text-align: center;
    font-family: "Alfa Slab One", serif; font-size: 88px; color: var(--ink-black);
    letter-spacing: 4px; -webkit-text-stroke: 2px var(--ink-white);
    text-shadow: 3px 4px 5px var(--shadow);
  }
  .for-sale {
    position: absolute; left: 0; top: 594px; width: 1206px; text-align: center;
    font-family: "Archivo Black", sans-serif; font-size: 56px; color: var(--ink-white);
    letter-spacing: 4px; text-shadow: 3px 4px 4px var(--shadow);
  }
  .phone-box {
    position: absolute; left: 320px; top: 674px; width: 580px; height: 66px;
    border-radius: 12px; background: rgba(127,188,182,0.75);
    border: 2px solid rgba(255,255,255,0.35);
    box-shadow: 2px 4px 8px rgba(0,0,0,0.4);
  }
  .phone-number {
    position: absolute; left: 320px; top: 670px; width: 580px; text-align: center;
    font-family: "Arimo", sans-serif; font-weight: 700; font-size: 58px;
    color: var(--ink-white); letter-spacing: 2px; text-shadow: 3px 4px 4px var(--shadow);
  }
</style>
</head>
<body>
<div class="canvas">
  <div class="sign-frame">
    <div class="sign-panel">
      <svg class="wood-grain" width="966" height="596" viewBox="0 0 966 596" aria-hidden="true">
        <g stroke="var(--seam)" stroke-width="4" opacity="0.85">
          <line x1="0" y1="6" x2="966" y2="6"/>
          <line x1="0" y1="118" x2="966" y2="118"/>
          <line x1="0" y1="232" x2="966" y2="232"/>
          <line x1="0" y1="344" x2="966" y2="344"/>
          <line x1="0" y1="448" x2="966" y2="448"/>
          <line x1="0" y1="560" x2="966" y2="560"/>
        </g>
      </svg>
    </div>
  </div>

  <svg class="layer" viewBox="0 0 1200 923">
    <g class="ornament" fill="var(--ink-white)" opacity="0.9">
      <rect x="256" y="276" width="116" height="28" rx="12" role="img" aria-label="Scroll flourish ornament"/>
      <rect x="832" y="276" width="116" height="28" rx="12" role="img" aria-label="Scroll flourish ornament"/>
      <rect x="148" y="662" width="128" height="62" rx="30" role="img" aria-label="Leaf scroll ornament"/>
      <rect x="924" y="662" width="132" height="62" rx="30" role="img" aria-label="Leaf scroll ornament"/>
    </g>
    <g class="hen-illustration" fill="var(--ink-white)" opacity="0.92">
      <rect x="196" y="450" width="176" height="126" rx="40" role="img" aria-label="White hen silhouette with fanned tail, facing right"/>
      <rect x="816" y="450" width="176" height="126" rx="40" role="img" aria-label="White hen silhouette with fanned tail, facing left"/>
    </g>
    <defs>
      <radialGradient id="eggGlow" cx="50%" cy="50%" r="50%">
        <stop offset="0%" stop-color="#dff1ee"/>
        <stop offset="60%" stop-color="var(--teal)"/>
        <stop offset="100%" stop-color="var(--teal-deep)"/>
      </radialGradient>
      <path id="arch" d="M 312 396 Q 604 232 896 396"/>
    </defs>
    <ellipse cx="604" cy="512" rx="96" ry="74" fill="url(#eggGlow)" stroke="#a8d6d0" stroke-width="4" role="img" aria-label="Teal sunburst egg badge"/>
    <text font-family="Oswald, sans-serif" font-weight="600" font-size="54" fill="var(--ink-white)" letter-spacing="3" style="filter: drop-shadow(2px 3px 3px rgba(0,0,0,0.55));">
      <textPath href="#arch" startOffset="50%" text-anchor="middle">FRESH FROM THE FARM</textPath>
    </text>
  </svg>

  <div class="brand">QUILL BEND<span class="brand-dot"></span>ACRES</div>
  <div class="tagline">ORGANIC • FREE RANGE</div>
  <div class="product">EGGS</div>
  <div class="for-sale">FOR SALE</div>
  <div class="phone-box"></div>
  <div class="phone-number">(555) 014 - 7293</div>
</div>
</body>
</html>
```